Dental Practice Billboard Design

We are a newer dental practice in need of a simple but appealing billboard for our growing dental practice to attract new patients. The practice is owned by husband and wife dentists and is family friendly in a small town in Kentucky. We try to be very friendly and caring to our patients. Would prefer a blue background for the billboard and our tooth logo to be prominent. We are partial to the Patua One font used in the image below but please feel free to tweak it as you deem necessary. The shape of the uppercase D and lowercase g are why we like that font, so fonts with a similarly shaped “D” and “g” would work as well. Please include our phone number (606) 847-3962. Please see our website Harlowfamilydentistry.com for more info on the practice if needed. Thank you! Looking forward to seeing your creation.
Updates

The dimensions will be 12ft x 24ft (3.6576m x 7.3152m). Apologies for not including this in the original prompt. Thank you all for your submissions.

Industry/Entity Type

Dental

Font styles to use
Other font styles liked:
• Patua One

Colors
0054AA
0677BA
7BADD7
CADEEF
E8F1F8
0094D4
00A9DD
6FCCEA
C7EBF8
E9F6FB
00AB8E
00BBA5
67D7C9
C6EFE9
E9F9F6
59FF00
82FF00
B8FF75
E3FFCB
F4FFEA

Requirements
Must have
• Phone number, website, Logo, Practice name “Harlow Family Dentistry”
Should not have
• A tagline or slogan

```html
<!DOCTYPE html>
<html lang="en">
<head>
<meta charset="utf-8">
<title>Harlow Family Dentistry Billboard</title>
<link href="https://fonts.googleapis.com/css2?family=Patua+One&family=Poppins:wght@600;700&display=swap" rel="stylesheet">
<style>
  :root {
    --page: #ffffff;
    --navy: #13437a;
    --royal: #0054aa;
    --sky: #6fccea;
    --sky-deep: #2ba3ea;
    --lime: #82ff00;
    --lime-text: #a6e23c;
    --white: #ffffff;
  }
  html, body {
    margin: 0;
    width: 901px;
    height: 1200px;
    overflow: hidden;
    background: var(--page);
  }
  .billboard {
    position: absolute;
    left: 131px;
    top: 198px;
    width: 638px;
    height: 319px;
    overflow: hidden;
    background: linear-gradient(100deg, var(--navy) 0%, #0a4d98 45%, var(--royal) 100%);
  }
  .billboard-art {
    position: absolute;
    inset: 0;
    width: 100%;
    height: 100%;
  }
  .brand-mark {
    position: absolute;
    left: 20px;
    top: 58px;
    width: 80px;
    height: 80px;
    border-radius: 50%;
    background: var(--white);
  }
  .brand {
    position: absolute;
    left: 115px;
    top: 52px;
    font-family: "Patua One", serif;
    color: var(--white);
  }
  .brand-name {
    font-size: 60px;
    line-height: 1;
  }
  .brand-sub {
    font-size: 30px;
    line-height: 1.1;
    margin-top: 6px;
  }
  .divider {
    position: absolute;
    left: 0;
    top: 187px;
    width: 355px;
    height: 3px;
    background: linear-gradient(90deg, rgba(111,204,234,0.2), var(--sky) 60%, rgba(111,204,234,0.5));
  }
  .call {
    position: absolute;
    left: 32px;
    top: 200px;
    width: 316px;
    display: flex;
    align-items: center;
    gap: 14px;
    font-family: "Poppins", sans-serif;
    font-weight: 700;
    font-size: 24px;
    line-height: 32px;
    color: var(--lime-text);
    letter-spacing: 0.5px;
  }
  .call-rule {
    flex: 1;
    height: 1px;
    background: var(--lime);
  }
  .phone {
    position: absolute;
    left: 31px;
    top: 232px;
    font-family: "Poppins", sans-serif;
    font-weight: 700;
    font-size: 42px;
    line-height: 1.2;
    color: var(--white);
    letter-spacing: -0.5px;
  }
  .website {
    position: absolute;
    left: 33px;
    top: 288px;
    font-family: "Poppins", sans-serif;
    font-weight: 600;
    font-size: 15px;
    line-height: 1.2;
    color: var(--white);
  }
</style>
</head>
<body>
  <section class="billboard">
    <svg class="billboard-art" viewBox="0 0 638 319" preserveAspectRatio="none">
      <defs>
        <linearGradient id="swoosh" x1="0" y1="0" x2="0.3" y2="1">
          <stop offset="0" stop-color="#6fccea"/>
          <stop offset="1" stop-color="#2ba3ea"/>
        </linearGradient>
        <linearGradient id="smile" x1="0" y1="0" x2="1" y2="1">
          <stop offset="0" stop-color="#c79479"/>
          <stop offset="0.45" stop-color="#c9505c"/>
          <stop offset="0.7" stop-color="#e4ddd4"/>
          <stop offset="1" stop-color="#c98f74"/>
        </linearGradient>
      </defs>
      <path class="swoosh" d="M314,0 C322,120 385,250 475,319 L638,319 L638,0 Z" fill="url(#swoosh)"/>
      <path class="smile-photo" role="img" aria-label="Close-up photo of a smiling mouth with white teeth and pink lips"
            d="M336,0 C352,125 455,265 638,319 L638,0 Z" fill="url(#smile)"/>
    </svg>

    <div class="brand-mark"></div>
    <div class="brand">
      <div class="brand-name">Harlow</div>
      <div class="brand-sub">Family Dentistry</div>
    </div>

    <div class="divider"></div>

    <div class="call"><span class="call-rule"></span>CALL US<span class="call-rule"></span></div>
    <div class="phone">(606) 847-3962</div>
    <div class="website">Harlowfamilydentistry.com</div>
  </section>
</body>
</html>
```